Refer a Friend A5 Flyer for Healthcare Staff

We need an A5 flyer that we can hand out to existing and new staff members promoting our Refer a friend Scheme. We need the leaflet to encourage staff to talk to their family and friends about joining our Healthcare Agency, which provides staff to local care related establishments. Using our logo and brand colours blue and green, as per our website, the final design will need to clearly convey the benefits and attractions of referring additional staff to the team. In addition is the promotion of our Friendloop page, requesting staff to like the page and to like and share various posts.

Target Market(s)

Healthcare and potential Healthcare Staff

Industry/Entity Type

Healthcare

Colors
33b8a4
3277b5

Requirements
Must have
• Company Logo, Brand colours,
• text; "Refer a Friend and receive a £50 Bonus after just 1 completed shift"
• text; "3 easy steps to refer a friend, 1 Fill out your name on the back of your Business Card 2 Hand the card to your friend or any person you wish to refer, 3 ask your friend to present the card to us when they attend their interview"
• text; "Like and share any of our Open Days on Friendloop for a chance to win a prize, you can find us easily by searching @CarewellPlacementGroup"
• text; "Like our Page to stay up to date with our events and offers"
Nice to have
• care worker / elderly care / support worker pictures
• Content / pics from website www.carewellplacementgroup.co.uk

```html
<!DOCTYPE html>
<html lang="en">
<head>
<meta charset="utf-8">
<title>Refer a Friend Flyer – Carewell Placement Group</title>
<link rel="stylesheet" href="https://fonts.googleapis.com/css2?family=Fira+Sans:wght@400;500;600;700&display=swap">
<style>
  :root{
    --teal:#33b8a4;
    --blue:#3277b5;
    --ink:#555a5e;
    --stage:#c3c6c7;
    --white:#ffffff;
  }
  *{margin:0;padding:0;box-sizing:border-box;}
  html,body{width:1200px;height:799px;overflow:hidden;background:var(--stage);font-family:"Fira Sans",sans-serif;}
  .canvas{position:relative;width:1200px;height:799px;}
  .flyer{position:absolute;top:104px;width:417px;height:592px;background:var(--white);overflow:hidden;}
  .flyer--front{left:169px;}
  .flyer--back{left:614px;}
  .flyer__shapes{position:absolute;inset:0;width:417px;height:592px;}
  .photo{position:absolute;border:4px solid var(--white);}
  .photo--garden{left:4px;top:339px;width:144px;height:100px;border-radius:6px 40px 6px 6px;background:linear-gradient(135deg,#5d7f3b,#9db2c9 55%,#d9b86a);}
  .photo--wheelchair{left:4px;top:442px;width:144px;height:100px;border-radius:6px 6px 6px 40px;background:linear-gradient(135deg,#6f8e4a,#b7a892 50%,#d9503e 75%,#7a9a55);}
  .photo--companions{left:153px;top:389px;width:145px;height:100px;border-radius:6px 6px 40px 6px;background:linear-gradient(90deg,#cbb29a,#a88f78 45%,#f1f1f1 70%,#c9b9a4);}
  .photo--team{position:absolute;left:240px;top:368px;width:177px;height:206px;background:linear-gradient(180deg,#eef3f7,#d3e0ea 50%,#e9eff4);}
  .headline{position:absolute;right:9px;color:var(--white);font-weight:600;font-size:20px;line-height:26px;text-align:right;letter-spacing:.2px;}
  .headline--top{top:242px;}
  .headline--bottom{top:394px;line-height:25.5px;}
  .bonus{position:absolute;left:309px;top:292px;width:100px;height:100px;border-radius:50%;background:var(--teal);color:var(--white);font-weight:700;text-align:center;}
  .bonus__text{position:absolute;left:0;top:18px;width:100%;transform:rotate(12deg);font-size:27px;line-height:27px;}
  .brand{position:absolute;display:flex;align-items:center;gap:7px;color:var(--blue);font-weight:400;font-size:19px;line-height:21px;}
  .brand__dot{width:16px;height:16px;border-radius:50%;background:var(--teal);flex:none;}
  .flyer--front .brand{left:240px;top:526px;}
  .flyer--back .brand{left:10px;top:526px;}
  .steps-title{position:absolute;left:10px;top:94px;height:21px;padding:0 7px;background:var(--teal);color:var(--white);font-weight:600;font-size:16.5px;line-height:21px;}
  .steps{position:absolute;left:10px;top:124px;list-style:none;color:var(--ink);font-weight:600;font-size:11.5px;line-height:23.5px;}
  .steps li{position:relative;padding-left:10px;}
  .steps li::before{content:"";position:absolute;left:0;top:9px;width:4px;height:4px;background:var(--teal);}
  .steps .indent{padding-left:20px;}
  .steps .indent::before{display:none;}
  .social-note{position:absolute;right:6px;top:266px;text-align:right;color:var(--ink);font-weight:600;font-size:11.5px;line-height:23.5px;}
  .social-note__handle{display:block;margin-top:3px;color:var(--teal);font-size:14px;font-weight:600;}
  .like-box{position:absolute;left:0;top:386px;width:179px;height:78px;background:var(--blue);color:var(--white);font-weight:600;font-size:14px;line-height:21px;padding:10px 0 0 10px;}
  .like-icon{position:absolute;left:178px;top:386px;width:56px;height:60px;}
</style>
</head>
<body>
<main class="canvas">

  <section class="flyer flyer--front" aria-label="Flyer front">
    <svg class="flyer__shapes" viewBox="0 0 417 592">
      <defs>
        <linearGradient id="panelGrad" x1="0" y1="0" x2="1" y2="0">
          <stop offset="0" stop-color="#33b8a4"/>
          <stop offset="1" stop-color="#3277b5"/>
        </linearGradient>
        <linearGradient id="heroGrad" x1="0" y1="0" x2="1" y2="1">
          <stop offset="0" stop-color="#8fc0d6"/>
          <stop offset=".35" stop-color="#7fa7c7"/>
          <stop offset=".6" stop-color="#9cc25a"/>
          <stop offset="1" stop-color="#d8d3cf"/>
        </linearGradient>
      </defs>
      <g role="img" aria-label="Photo: smiling care worker holding hands with an elderly woman outdoors">
        <path d="M0,0 H417 V212 C330,210 250,235 170,272 C110,300 50,318 0,318 Z" fill="url(#heroGrad)"/>
      </g>
      <path d="M0,0 H190 C150,10 110,30 0,92 Z" fill="url(#panelGrad)"/>
      <path d="M96,55 C150,30 200,10 255,0 H270 C200,14 150,32 96,55 Z" fill="#ffffff"/>
      <path d="M0,318 C60,318 120,300 180,272 C260,235 330,212 417,212 V505 C320,505 220,535 110,592 H0 Z" fill="url(#panelGrad)"/>
      <path d="M150,288 C230,245 330,214 417,218 V224 C330,222 240,250 150,288 Z" fill="#ffffff" opacity=".85"/>
      <path d="M0,322 C60,330 120,320 170,300 C110,330 50,340 0,338 Z" fill="#e7e9ea"/>
      <path d="M90,592 C200,530 320,505 417,505 V592 Z" fill="#ffffff"/>
      <path d="M80,592 C190,532 300,500 417,498 V505 C310,508 200,540 110,592 Z" fill="#e4e6e7"/>
      <path d="M60,592 C100,572 130,560 150,553 C130,566 110,578 95,592 Z" fill="#33b8a4"/>
    </svg>

    <h2 class="headline headline--top">Refer A Friend<br>And Receive A</h2>
    <div class="bonus"><div class="bonus__text">£50<br>Bonus</div></div>
    <p class="headline headline--bottom">After Just 1<br>Completed<br>Shift</p>

    <div class="photo photo--garden" role="img" aria-label="Photo: elderly man in a wheelchair with a carer in a garden"></div>
    <div class="photo photo--wheelchair" role="img" aria-label="Photo: elderly woman in a wheelchair outdoors with a carer"></div>
    <div class="photo photo--companions" role="img" aria-label="Photo: care worker chatting with an elderly woman indoors"></div>

    <div class="brand"><span class="brand__dot"></span><span>Carewell<br>Placement Group</span></div>
  </section>

  <section class="flyer flyer--back" aria-label="Flyer back">
    <svg class="flyer__shapes" viewBox="0 0 417 592" aria-hidden="true">
      <defs>
        <linearGradient id="backGrad" x1="0" y1="0" x2="1" y2="0">
          <stop offset="0" stop-color="#3277b5"/>
          <stop offset="1" stop-color="#33b8a4"/>
        </linearGradient>
      </defs>
      <path d="M200,0 H417 V92 C350,85 290,55 200,0 Z" fill="url(#backGrad)"/>
      <path d="M198,0 H212 C290,50 350,80 417,92 V96 C340,88 280,60 198,0 Z" fill="#ffffff"/>
      <path d="M0,500 C90,465 200,470 300,530 C340,555 380,575 417,592 H380 C300,540 200,490 100,490 C60,490 30,496 0,506 Z" fill="url(#backGrad)"/>
      <path d="M0,515 C80,495 180,500 260,540 C290,555 310,570 330,592 H318 C290,565 200,510 100,508 C60,508 30,512 0,520 Z" fill="#dfe2e3"/>
      <path d="M330,560 C370,575 395,585 417,585 V592 H350 Z" fill="#33b8a4"/>
    </svg>

    <h2 class="steps-title">3 Easy Steps To Refer A Friend</h2>
    <ul class="steps">
      <li>1 Fill Out Your Name On The Back Of Your Business Card</li>
      <li>2 Hand The Card To Your Friend Or</li>
      <li class="indent">Any Person You Wish To Refer,</li>
      <li>3 Ask Your Friend To Present The Card</li>
      <li class="indent">To Us When They Attend Their Interview"</li>
    </ul>

    <p class="social-note">Like And Share Any Of Our Open Days On<br>Friendloop For A Chance To Win A Prize,<br>You Can Find Us Easily By Searching<span class="social-note__handle">@CarewellPlacementGroup</span></p>

    <p class="like-box">Like Our Page To<br>Stay Up To Date With<br>Our Events And Offers</p>
    <svg class="like-icon" viewBox="0 0 56 60" aria-hidden="true">
      <rect x="1" y="27" width="12" height="26" fill="#33b8a4"/>
      <path d="M15,27 L24,14 C26,10 26,6 27,2 C33,2 35,8 33,18 H48 C53,18 54,24 50,27 C54,29 54,34 50,36 C53,38 53,43 49,45 C52,48 50,53 45,53 H15 Z" fill="#ffffff" stroke="#3277b5" stroke-width="2.5" stroke-linejoin="round"/>
    </svg>

    <div class="photo--team" role="img" aria-label="Photo: group of healthcare staff in white uniforms joining hands in the air"></div>

    <div class="brand"><span class="brand__dot"></span><span>Carewell<br>Placement Group</span></div>
  </section>

</main>
</body>
</html>
```